Velvet Lantern rebranding my business with a new business card

I have my new logo and now I need a refresher on my business cards. I really want something fun and fresh. I like black background or anything to make the color pop.
Logo
Name: Velvet Lantern
Contact Info as stated below:
Mara Pelkin
519-555-0147
Logo
Name: Velvet Lantern
Mara Pelkin
519-555-0147
fb.me/VelvetLanternbyMara
Instagram: @VelvetLanternbyMara

Industry/Entity Type

Business

Contact Information for Business Card

double-sided. Logo on one side. Contact info on the other.

Requirements
Must have
• Logo
• Name: Velvet Lantern
• Contact Info as stated below:
• Mara Pelkin
• 519-555-0147
• fb.me/VelvetLanternbyMara
• fb.me/VelvetLanternbyMara

```html
<!DOCTYPE html>
<html lang="en">
<head>
<meta charset="utf-8">
<title>Velvet Lantern – Business Card</title>
<link href="https://fonts.googleapis.com/css2?family=Mountains+of+Christmas:wght@700&family=Poppins:wght@400&display=swap" rel="stylesheet">
<style>
  :root {
    --backdrop: #e4e4e4;
    --card-white: #ffffff;
    --band-teal: #33b8a3;
    --back-teal: #20b39e;
    --ink: #555555;
    --icon-teal: #2fb8a1;
    --ring-pink: #f0a7b8;
    --logo-ink: #1f7f72;
    --outline: #222222;
  }
  * { margin: 0; padding: 0; box-sizing: border-box; }
  html, body { width: 1200px; height: 1000px; overflow: hidden; }
  body { background: var(--backdrop); position: relative; font-family: "Poppins", sans-serif; }

  .card { position: absolute; left: 239px; width: 698px; height: 398px; border-radius: 18px; overflow: hidden; }
  .card--front { top: 82px; background: var(--card-white); }
  .card--back { top: 520px; background: var(--back-teal); }

  .name-band { position: absolute; left: 0; right: 0; top: 119px; height: 108px; background: var(--band-teal); }
  .band-label {
    position: absolute; top: 30px; color: #fff;
    font-family: "Mountains of Christmas", serif; font-weight: 700; font-size: 34px; letter-spacing: 1px;
  }
  .band-label--name { left: 27px; }
  .band-label--role { left: 479px; }

  .logo-badge {
    position: absolute; width: 202px; height: 202px; border-radius: 50%;
    background: #fff; border: 2px solid var(--outline);
    display: flex; align-items: center; justify-content: center;
  }
  .logo-badge::after {
    content: ""; position: absolute; inset: 8px; border-radius: 50%;
    border: 2px solid var(--ring-pink);
  }
  .card--front .logo-badge { left: 245px; top: 66px; }
  .card--back .logo-badge { left: 249px; top: 98px; }
  .logo-name {
    font-family: "Mountains of Christmas", serif; font-weight: 700; font-size: 30px;
    color: var(--logo-ink); text-align: center; line-height: 1.05;
  }

  .contact { position: absolute; top: 294px; left: 0; right: 0; font-size: 16px; color: var(--ink); }
  .contact-row { position: absolute; display: flex; align-items: center; height: 20px; }
  .contact-row--first { top: 0; }
  .contact-row--second { top: 28px; }
  .contact-left { position: absolute; right: 373px; white-space: nowrap; }
  .contact-icons { position: absolute; left: 333px; display: flex; gap: 9px; }
  .contact-right { position: absolute; left: 375px; white-space: nowrap; }
  .icon { width: 13px; height: 13px; border-radius: 2px; background: var(--icon-teal); display: block; }
  .icon svg { display: block; }
</style>
</head>
<body>
  <section class="card card--front">
    <div class="name-band">
      <span class="band-label band-label--name">Mara Pelkin</span>
      <span class="band-label band-label--role">Owner</span>
    </div>
    <div class="logo-badge">
      <span class="logo-name">Velvet<br>Lantern</span>
    </div>
    <div class="contact">
      <div class="contact-row contact-row--first" style="left:0;right:0;">
        <span class="contact-left" style="top:0;">519-555-0147</span>
        <span class="contact-icons" style="top:3px;">
          <span class="icon"><svg viewBox="0 0 13 13" width="13" height="13"><path d="M4 3 L5.5 4.8 L4.8 5.8 Q5.6 7.5 7.2 8.2 L8.2 7.5 L10 9 L9 10.2 Q5.5 10 2.8 4.2 Z" fill="#fff"/></svg></span>
          <span class="icon"></span>
        </span>
        <span class="contact-right" style="top:0;">me/VelvetLanternbyMara</span>
      </div>
      <div class="contact-row contact-row--second" style="left:0;right:0;">
        <span class="contact-left" style="top:0;">hello@marapelkin.com</span>
        <span class="contact-icons" style="top:3px;">
          <span class="icon"><svg viewBox="0 0 13 13" width="13" height="13"><rect x="2.5" y="3.5" width="8" height="6" fill="#fff"/><path d="M2.5 3.5 L6.5 6.8 L10.5 3.5" fill="none" stroke="#2fb8a1" stroke-width="1"/></svg></span>
          <span class="icon"></span>
        </span>
        <span class="contact-right" style="top:0;">@VelvetLanternbyMara</span>
      </div>
    </div>
  </section>

  <section class="card card--back">
    <div class="logo-badge">
      <span class="logo-name">Velvet<br>Lantern</span>
    </div>
  </section>
</body>
</html>
```